Whispers From Distant Stars Poster

So Last year One of the Great Designers from here Came up with a poster for my Events... But Now it is Time to freshen it up.. I have attached the original poster.. I would like the Same wording.. Same Picture of me,. Just fresh Design and colours for the new event year ahead.
This Poster Will be used in Theatres and Hall to Advertise our Event so it needs to stand out but still remain classy
I would Also need The Final Version to be delivered in PhotoShop Version so That I Can Alter Things like the Venue Name, Date, and Ticket Details,, As they change all the time.
Events

```html
<!DOCTYPE html>
<html lang="en">
<head>
<meta charset="utf-8">
<title>Whispers From Distant Stars – Poster</title>
<link href="https://fonts.googleapis.com/css2?family=Bebas+Neue&family=Oswald:wght@300;400;500&family=Roboto:wght@400;700&display=swap" rel="stylesheet">
<style>
  :root{
    --midnight:#0d0a1f;
    --indigo:#1c1640;
    --plum:#3a1f4f;
    --violet-glow:#6b4a9a;
    --gold:#d9b46a;
    --gold-light:#f3dfa8;
    --ivory:#f7f2e6;
    --mist:#b9b2cf;
  }
  html,body{margin:0;padding:0;overflow:hidden;background:var(--midnight);}
  .poster{
    position:relative;width:802px;height:1200px;overflow:hidden;
    background:
      radial-gradient(ellipse 70% 45% at 80% 30%,rgba(107,74,154,.55),rgba(107,74,154,0) 70%),
      linear-gradient(170deg,var(--indigo) 0%,var(--plum) 45%,var(--indigo) 70%,var(--midnight) 100%);
    font-family:'Oswald',sans-serif;color:var(--ivory);
  }
  .portrait{
    position:absolute;right:0;top:0;width:470px;height:800px;
    background:
      radial-gradient(ellipse 30% 22% at 52% 30%,rgba(226,190,180,.75),rgba(226,190,180,0) 75%),
      radial-gradient(ellipse 60% 40% at 55% 78%,rgba(20,18,38,.9),rgba(20,18,38,0) 75%),
      linear-gradient(90deg,rgba(58,31,79,0) 0%,rgba(150,130,190,.35) 45%,rgba(150,130,190,.2) 100%);
    -webkit-mask-image:linear-gradient(180deg,#000 70%,transparent 100%);
    mask-image:linear-gradient(180deg,#000 70%,transparent 100%);
  }
  .frame{position:absolute;inset:22px;border:1px solid rgba(217,180,106,.45);pointer-events:none;}

  .title-block{position:absolute;left:56px;top:96px;width:380px;}
  .title-kicker{margin:0;font-weight:300;font-size:32px;letter-spacing:6px;line-height:1;color:var(--mist);}
  .title-main{
    margin:14px 0 0;font-family:'Bebas Neue',sans-serif;font-weight:400;font-size:128px;line-height:.88;letter-spacing:2px;
    background:linear-gradient(180deg,var(--gold-light) 0%,var(--gold) 60%,#b08a45 100%);
    -webkit-background-clip:text;background-clip:text;color:transparent;
  }
  .title-rule{width:120px;height:2px;margin:26px 0 0;background:var(--gold);}
  .subtitle{margin:22px 0 0;font-weight:400;font-size:20px;letter-spacing:8px;line-height:1.6;color:var(--ivory);}

  .billing{position:absolute;left:56px;right:56px;top:812px;padding-left:24px;border-left:3px solid var(--gold);}
  .billing-role{margin:0;font-weight:400;font-size:20px;letter-spacing:7px;line-height:1;color:var(--gold);}
  .billing-name{margin:10px 0 0;font-family:'Bebas Neue',sans-serif;font-weight:400;font-size:108px;line-height:.9;letter-spacing:2px;color:var(--ivory);}
  .date{margin:18px 0 0;font-weight:500;font-size:36px;line-height:1;color:var(--gold-light);}
  .venue{margin:12px 0 0;font-weight:300;font-size:26px;line-height:1;letter-spacing:2px;color:var(--ivory);}
  .tickets{margin:22px 0 0;font-family:'Roboto',sans-serif;font-size:17px;line-height:1.5;color:var(--mist);}
  .tickets strong{color:var(--gold-light);font-weight:700;}
  .tickets .hl{color:var(--ivory);}
</style>
</head>
<body>
<main class="poster">
  <div class="portrait" role="img" aria-label="Photograph of the medium in a dark suit and open white shirt, reaching a hand forward"></div>
  <div class="frame"></div>

  <header class="title-block">
    <p class="title-kicker">WHISPERS FROM</p>
    <h1 class="title-main">DISTANT<br>STARS</h1>
    <div class="title-rule"></div>
    <p class="subtitle">AN EVENING OF<br>MEDIUMSHIP</p>
  </header>

  <section class="billing">
    <p class="billing-role">RENOWNED SPIRITUALIST MEDIUM</p>
    <h2 class="billing-name">RHYS CALLOWAY</h2>
    <p class="date">THURSDAY 23RD NOV | AT 7PM</p>
    <p class="venue">LARKFIELD PLAYHOUSE BRYNTEG</p>
    <p class="tickets">FOR TICKETS <strong>£10</strong> FROM BOX OFFICE <span class="hl">01632 960418</span><br>OR <span class="hl">LARKFIELDPLAYHOUSE.CO.UK</span></p>
  </section>
</main>
</body>
</html>
```